Larkfell PowerPoint Slide Deck

We have created a new company the provides workforce solutions for rural healthcare providers in the United States. We have a website located at: https://larkfellsolutions.example. Now we need a PowerPoint template that Larkfell employees can use to support in-person and virtual presentations. We want the final PowerPoint template/master slides to be consistent thematically with the Larkfell website, with an emphasis on simplicity -- clean, subtle, professional, relatively stark and with a white background dominant. It should use the Larkfell color scheme, logo and logo pattern. The product we select will need a cover/title slide as well as templates for a variety of slide layouts. Please refer to the Larkfell Style Guide attached to this request.

```html
<!DOCTYPE html>
<html lang="en">
<head>
<meta charset="utf-8">
<title>Larkfell Slide Deck Overview</title>
<link href="https://fonts.googleapis.com/css2?family=Rubik:wght@400;500;600&display=swap" rel="stylesheet">
<style>
:root{
  --red:#e8474a;
  --red-soft:#ef6a6c;
  --pink:#f9d3d4;
  --ink:#1f1f1f;
  --muted:#5c5c5c;
  --white:#ffffff;
  --photo-a:#dde5ea;
  --photo-b:#aebcc6;
  --skin:#d8b7a4;
  --teal:#5fb7a5;
}
*{box-sizing:border-box;margin:0;padding:0}
html,body{width:739px;height:1200px;overflow:hidden;background:var(--white)}
body{font-family:"Rubik",sans-serif;color:var(--ink);position:relative}
.slide{position:absolute;width:228px;height:128px;background:var(--white);overflow:hidden;box-shadow:0 1px 2px rgba(0,0,0,.18)}
.abs{position:absolute}
.photo{position:absolute;background:linear-gradient(135deg,var(--photo-a),var(--photo-b))}
.photo.warm{background:linear-gradient(135deg,#e9dccf,#b9a293)}
.photo.scrubs{background:linear-gradient(135deg,#8fcfc1,#4f9f90)}
.photo.blue{background:linear-gradient(135deg,#9fc4e0,#5d8fb8)}
.photo.dark{background:linear-gradient(135deg,#6f625b,#3b3330)}
.logo{position:absolute;display:flex;align-items:center;gap:3px;font-weight:600;font-size:8px;color:var(--ink);white-space:nowrap}
.logo::before{content:"";width:8px;height:8px;background:var(--red);display:block}
.logo.lg{font-size:12px;gap:4px}
.logo.lg::before{width:13px;height:13px}
.title{position:absolute;font-size:9.5px;line-height:1.25;font-weight:400;color:var(--ink)}
.red{color:var(--red)}
.white{color:var(--white)}
.kicker{position:absolute;font-size:7px;color:var(--red)}
.t{position:absolute;font-size:3.1px;line-height:1.6;color:var(--muted)}
.t.w{color:#fde9e9}
.box{position:absolute;background:var(--red)}
.card{position:absolute;background:var(--white);box-shadow:0 1px 3px rgba(0,0,0,.15);border-radius:2px}
.ico{position:absolute;width:10px;height:10px;border:1.2px solid var(--red);border-radius:3px}
.glyph{width:5px;height:5px;background:var(--red);border-radius:1.5px;display:block}
</style>
</head>
<body>

<!-- Row 1 -->
<section class="slide" style="left:17px;top:14px">
  <div class="photo" role="img" aria-label="Doctor in white coat holding a red stethoscope" style="left:92px;top:-10px;width:150px;height:110px;border-radius:60% 0 40% 70% / 60% 0 60% 50%"></div>
  <div class="logo lg" style="left:17px;top:24px">Larkfell</div>
  <div class="title" style="left:18px;top:73px;font-size:11px">Larkfell<br>Presentation</div>
  <div class="kicker" style="left:18px;top:104px">Project 01</div>
</section>

<section class="slide" style="left:258px;top:14px">
  <div class="photo" role="img" aria-label="Three masked medical staff in a clinic" style="left:0;top:0;width:228px;height:84px"></div>
  <div class="box" style="left:13px;top:77px;width:77px;height:33px;border-radius:2px"></div>
  <div class="title white" style="left:13px;top:82px;width:77px;text-align:center;font-size:7.5px">Healing Health<br>Care Together</div>
  <div class="t" style="left:102px;top:93px;width:112px">Our teams bring steady, skilled support to rural clinics so local patients get care close to home, every day of the week, with trusted staff.</div>
</section>

<section class="slide" style="left:498px;top:14px">
  <div class="logo" style="left:19px;top:13px">Larkfell</div>
  <div class="title" style="left:19px;top:30px;font-size:10px">Best of Care,<br>Close to Home</div>
  <div class="ico" style="left:100px;top:24px;border-radius:50%"></div>
  <div class="abs red" style="left:99px;top:38px;font-size:3px">Genius In Healthcare</div>
  <div class="t" style="left:99px;top:43px;width:52px">Skilled staff placed where rural clinics need them most.</div>
  <div class="ico" style="left:159px;top:24px;border-radius:50%"></div>
  <div class="abs red" style="left:158px;top:38px;font-size:3px">Genius In Healthcare</div>
  <div class="t" style="left:158px;top:43px;width:52px">Flexible support plans built around local teams.</div>
  <div class="photo warm" role="img" aria-label="Caregivers smiling with an elderly patient and a child" style="left:0;top:64px;width:228px;height:64px"></div>
</section>

<!-- Row 2 -->
<section class="slide" style="left:17px;top:144px">
  <div class="photo" role="img" aria-label="Smiling doctor holding a clipboard" style="left:18px;top:17px;width:72px;height:95px;border-radius:8px"></div>
  <div class="abs" style="left:80px;top:7px;width:22px;height:22px;border-radius:50%;background:linear-gradient(180deg,#fbd6d6,var(--red))"></div>
  <div class="abs" style="left:10px;top:99px;width:22px;height:22px;border-radius:50%;background:linear-gradient(180deg,#fbd6d6,var(--red))"></div>
  <div class="kicker" style="left:104px;top:32px;font-size:8px">Table Contents</div>
  <div class="abs" style="left:104px;top:48px;font-size:3.6px;line-height:3;color:var(--ink)">01. About Us<br>02. Our Journey<br>03. Our CEO<br>04. Meet Our Doctor<br>05. Relax Time</div>
  <div class="abs" style="left:162px;top:48px;font-size:3.6px;line-height:3;color:var(--ink)">06. Meet Our Doctors<br>07. Our Tables<br>08. Infographics<br>09. Contact Us</div>
</section>

<section class="slide" style="left:258px;top:144px">
  <div class="logo" style="left:21px;top:17px">Larkfell</div>
  <div class="title" style="left:22px;top:36px">Meet The Doctor<br>Specialist</div>
  <div class="t" style="left:22px;top:60px;width:88px">Our specialists partner with local clinics to give patients expert care without long trips to distant city hospitals or crowded centers.</div>
  <div class="abs red" style="left:22px;top:95px;font-size:3.3px">Dr. Nora Vale</div>
  <div class="abs" style="left:22px;top:101px;font-size:3.3px">Virology Sp.</div>
  <div class="photo" role="img" aria-label="Smiling female doctor with stethoscope" style="left:142px;top:22px;width:86px;height:106px"></div>
  <div class="box" style="left:124px;top:10px;width:20px;height:20px;border-radius:2px"></div>
  <svg class="abs" style="left:129px;top:15px" width="10" height="10" viewBox="0 0 10 10"><path d="M5 8.5 1.4 5A2.1 2.1 0 0 1 5 2.3 2.1 2.1 0 0 1 8.6 5Z" fill="none" stroke="#fff" stroke-width=".9"/></svg>
</section>

<section class="slide" style="left:498px;top:144px">
  <div class="box" style="left:0;top:0;width:228px;height:128px"></div>
  <div class="photo blue" role="img" aria-label="Doctor giving a high five to a young boy" style="left:0;top:0;width:97px;height:128px"></div>
  <div class="title white" style="left:120px;top:27px;font-size:10.5px">Working For Your<br>Better Health</div>
  <div class="card" style="left:82px;top:68px;width:36px;height:41px"></div>
  <div class="card" style="left:127px;top:68px;width:36px;height:41px"></div>
  <div class="card" style="left:173px;top:68px;width:36px;height:41px"></div>
  <div class="ico" style="left:95px;top:74px;border-radius:50%"></div>
  <div class="ico" style="left:140px;top:74px"></div>
  <div class="ico" style="left:186px;top:74px;border-radius:50%"></div>
  <div class="abs red" style="left:82px;top:89px;width:36px;text-align:center;font-size:3px;line-height:1.3">Bringing The Future Of Healthcare</div>
  <div class="abs red" style="left:127px;top:89px;width:36px;text-align:center;font-size:3px;line-height:1.3">A True Devotion to Healing</div>
  <div class="abs red" style="left:173px;top:89px;width:36px;text-align:center;font-size:3px;line-height:1.3">A Family Of Hospitals For Your Family</div>
</section>

<!-- Row 3 -->
<section class="slide" style="left:17px;top:274px">
  <div class="photo" role="img" aria-label="Doctor with arms crossed holding a stethoscope" style="left:13px;top:10px;width:86px;height:118px;border-radius:8px 8px 0 0"></div>
  <div class="box" style="left:93px;top:27px;width:19px;height:19px;border-radius:2px"></div>
  <div class="abs" style="left:98px;top:32px;width:9px;height:5px;border:1px solid #fff;border-radius:3px;transform:rotate(-40deg);margin-top:2px"></div>
  <div class="kicker" style="left:120px;top:32px;font-size:6px">About Us</div>
  <div class="title" style="left:120px;top:41px;font-size:6.5px;font-weight:500">Transforming Rural<br>Healthcare with Tailored<br>Solutions for Success</div>
  <div class="t" style="left:120px;top:71px;width:95px">Larkfell partners with rural healthcare groups to address staffing, distance and infrastructure needs. Our clients see smoother operations, better engagement and the strength to compete with larger systems.</div>
</section>

<section class="slide" style="left:258px;top:274px">
  <div class="box" style="left:0;top:0;width:228px;height:128px"></div>
  <div class="abs" style="left:0;top:0;width:100px;height:128px;background:var(--white);clip-path:polygon(0 0,100% 0,62% 100%,0 100%)"></div>
  <div class="photo warm" role="img" aria-label="Nurse with an elderly man in a wheelchair" style="left:8px;top:4px;width:74px;height:124px;clip-path:polygon(12% 0,100% 0,78% 100%,0 100%)"></div>
  <div class="card" style="left:76px;top:18px;width:125px;height:42px"></div>
  <div class="title" style="left:86px;top:28px;font-size:8.5px">A Personal Relationship<br>With Medical Excellence</div>
  <div class="t w" style="left:95px;top:71px;width:112px;line-height:2.8">Every placement is built on trust between our staff, your team and the patients you serve. We listen first, plan together and stay close long after the first shift begins.</div>
</section>

<section class="slide" style="left:498px;top:274px">
  <div class="box" style="left:0;top:64px;width:228px;height:64px"></div>
  <div class="card" style="left:20px;top:18px;width:57px;height:92px"></div>
  <div class="card" style="left:85px;top:18px;width:57px;height:92px"></div>
  <div class="card" style="left:151px;top:18px;width:57px;height:92px"></div>
  <div class="abs" style="left:20px;top:28px;width:57px;text-align:center;font-size:3.6px">Insurance 1</div>
  <div class="abs" style="left:85px;top:28px;width:57px;text-align:center;font-size:3.6px">Insurance 2</div>
  <div class="abs" style="left:151px;top:28px;width:57px;text-align:center;font-size:3.6px">Insurance 3</div>
  <div class="abs red" style="left:20px;top:37px;width:57px;text-align:center;font-size:7.5px">$399/mo</div>
  <div class="abs red" style="left:85px;top:37px;width:57px;text-align:center;font-size:7.5px">$599/mo</div>
  <div class="abs red" style="left:151px;top:37px;width:57px;text-align:center;font-size:7.5px">$899/mo</div>
  <div class="box white" style="left:30px;top:53px;width:36px;height:6px;font-size:2.8px;text-align:center;line-height:6px">20% Cashback</div>
  <div class="box white" style="left:96px;top:53px;width:36px;height:6px;font-size:2.8px;text-align:center;line-height:6px">20% Cashback</div>
  <div class="box white" style="left:161px;top:53px;width:36px;height:6px;font-size:2.8px;text-align:center;line-height:6px">20% Cashback</div>
  <div class="abs" style="left:20px;top:65px;width:57px;text-align:center;font-size:3.4px">Services</div>
  <div class="abs" style="left:85px;top:65px;width:57px;text-align:center;font-size:3.4px">Services</div>
  <div class="abs" style="left:151px;top:65px;width:57px;text-align:center;font-size:3.4px">Services</div>
  <div class="t" style="left:27px;top:72px;width:46px;font-size:2.6px">• Weekly staff check-in<br>• On-call nurse cover<br>• Shared care records<br>• Monthly site review</div>
  <div class="t" style="left:92px;top:72px;width:46px;font-size:2.6px">• Weekly staff check-in<br>• On-call nurse cover<br>• Shared care records<br>• Monthly site review</div>
  <div class="t" style="left:158px;top:72px;width:46px;font-size:2.6px">• Weekly staff check-in<br>• On-call nurse cover<br>• Shared care records<br>• Monthly site review</div>
</section>

<!-- Row 4 -->
<section class="slide" style="left:17px;top:404px">
  <div class="box" style="left:0;top:0;width:128px;height:128px"></div>
  <div class="photo" role="img" aria-label="Doctor with arms crossed holding a stethoscope" style="left:128px;top:0;width:100px;height:128px"></div>
  <div class="title white" style="left:20px;top:28px;font-size:7.5px">About Us</div>
  <div class="title white" style="left:20px;top:38px;font-size:6.5px;font-weight:500">Transforming Rural<br>Healthcare with Tailored<br>Solutions for Success</div>
  <div class="t w" style="left:20px;top:67px;width:95px;line-height:2.2">Larkfell partners with rural healthcare groups to address staffing, distance and infrastructure needs. Our clients see smoother operations, better engagement and the strength to compete with larger systems.</div>
</section>

<section class="slide" style="left:258px;top:404px">
  <div class="logo" style="left:158px;top:15px">Larkfell</div>
  <div class="photo scrubs" role="img" aria-label="Clinician in green scrubs with arms crossed and stethoscope" style="left:16px;top:12px;width:98px;height:99px;border-radius:4px"></div>
  <div class="box" style="left:102px;top:37px;width:104px;height:78px;border-radius:2px"></div>
  <div class="title white" style="left:112px;top:47px;font-size:7px">Confidence For The<br>Good Life</div>
  <div class="t w" style="left:112px;top:66px;width:88px;line-height:2.6">Our clinicians bring calm, practiced hands to every visit, giving families the confidence to seek care early and often, right where they live.</div>
</section>

<section class="slide" style="left:498px;top:404px">
  <div class="logo" style="left:19px;top:17px">Larkfell</div>
  <div class="title" style="left:20px;top:33px;font-size:10px">Medicine Of The<br>Highest Order</div>
  <div class="t" style="left:20px;top:62px;width:90px;font-size:2.8px">Careful hiring, steady training and close follow-up keep our standards high at every clinic we support, large or small, near or far.</div>
  <div class="box" style="left:18px;top:88px;width:72px;height:20px;border-radius:2px"></div>
  <div class="abs white" style="left:24px;top:93px;font-size:7.5px">76%</div>
  <div class="abs white" style="left:47px;top:94px;font-size:2.8px;line-height:1.3">Dedication Beyond<br>Measure</div>
  <svg class="abs" style="left:121px;top:20px" width="90" height="90" viewBox="0 0 90 90">
    <circle cx="45" cy="45" r="37" fill="none" stroke="var(--pink)" stroke-width="5"/>
    <circle cx="45" cy="45" r="37" fill="none" stroke="var(--red)" stroke-width="5" stroke-dasharray="175 233" transform="rotate(-90 45 45)"/>
    <circle cx="9" cy="53" r="7" fill="#fff" stroke="var(--pink)" stroke-width="1"/>
  </svg>
  <div class="abs" style="left:126px;top:70px;width:9px;height:4px;border:1px solid var(--red);border-radius:3px;transform:rotate(-40deg)"></div>
  <div class="abs" style="left:136px;top:53px;width:60px;text-align:center;font-size:8.5px;line-height:1.3">All Our<br>Best</div>
</section>

<!-- Row 5 -->
<section class="slide" style="left:17px;top:534px">
  <div class="photo" role="img" aria-label="Stethoscope and pen on a notepad" style="left:16px;top:19px;width:48px;height:75px"></div>
  <div class="photo" role="img" aria-label="Doctor with arms crossed in white coat" style="left:47px;top:36px;width:54px;height:74px"></div>
  <div class="box" style="left:35px;top:83px;width:20px;height:20px;border-radius:2px"></div>
  <div class="abs" style="left:40px;top:88px;width:10px;height:9px;border:1px solid #fff;border-radius:1.5px"></div>
  <div class="kicker" style="left:112px;top:21px;font-size:8.5px;font-weight:500">OUR JOURNEY</div>
  <div class="title" style="left:112px;top:34px;font-size:6px">Empowering Rural Providers<br>Since Our Inception</div>
  <div class="t" style="left:112px;top:52px;width:100px">Founded on the belief that every community deserves quality care, Larkfell grew from close work with rural teams. We help providers reshape staffing and compete while keeping a local, personal touch. Over the years we have partnered with many clinics, building tailored plans that answer local needs and keep care steady in a changing field.</div>
</section>

<section class="slide" style="left:258px;top:534px">
  <div class="box" style="left:0;top:0;width:228px;height:128px"></div>
  <div class="abs" style="left:112px;top:-60px;width:170px;height:130px;border-radius:50%;background:var(--red-soft);opacity:.6"></div>
  <div class="abs" style="left:70px;top:90px;width:80px;height:80px;border-radius:50%;background:var(--red-soft);opacity:.5"></div>
  <div class="photo" role="img" aria-label="Doctor in white coat holding a red stethoscope" style="left:34px;top:10px;width:68px;height:108px;border-radius:34px"></div>
  <div class="title white" style="left:116px;top:29px;font-size:19px;line-height:1.3">Relax<br>Time</div>
  <div class="title white" style="left:116px;top:85px;font-size:7px">We continue after<br>30 minutes</div>
</section>

<section class="slide" style="left:498px;top:534px">
  <div class="logo" style="left:17px;top:15px">Larkfell</div>
  <div class="box" style="left:9px;top:34px;width:211px;height:68px;border-radius:3px"></div>
  <div class="photo warm" role="img" aria-label="Two smiling nurses in a clinic hallway" style="left:17px;top:54px;width:97px;height:74px;border-radius:3px 3px 0 0"></div>
  <div class="card" style="left:98px;top:17px;width:104px;height:53px"></div>
  <div class="kicker" style="left:98px;top:24px;width:104px;text-align:center;font-size:5.5px">Get in Touch</div>
  <svg class="abs" style="left:110px;top:35px" width="6" height="6" viewBox="0 0 10 10"><path d="M2 1 4 1 5 3.5 3.6 4.6A6 6 0 0 0 5.4 6.4L6.5 5 9 6V8Q9 9 8 9 1 8.5 1 2 1 1 2 1Z" fill="var(--red)"/></svg>
  <svg class="abs" style="left:110px;top:44px" width="6" height="6" viewBox="0 0 10 10"><rect x="1" y="2" width="8" height="6" fill="none" stroke="var(--red)"/><path d="M1 2 5 5.5 9 2" fill="none" stroke="var(--red)"/></svg>
  <svg class="abs" style="left:110px;top:53px" width="6" height="6" viewBox="0 0 10 10"><circle cx="5" cy="5" r="4" fill="none" stroke="var(--red)"/><path d="M1 5H9M5 1Q2 5 5 9Q8 5 5 1" fill="none" stroke="var(--red)" stroke-width=".7"/></svg>
  <div class="abs" style="left:121px;top:36px;font-size:3.4px;line-height:2.7">555-010-0700<br>info@larkfellsolutions.example<br>larkfellsolutions.example</div>
  <div class="abs white" style="left:124px;top:79px;font-size:5px">Contact Us</div>
  <div class="abs white" style="left:124px;top:86px;font-size:7px">Send Us Your Inquiries</div>
</section>

<!-- Row 6 -->
<section class="slide" style="left:17px;top:664px">
  <div class="box" style="left:178px;top:0;width:50px;height:128px"></div>
  <div class="title" style="left:23px;top:29px;font-size:10px">Confidence For<br>The Good Life</div>
  <div class="t" style="left:23px;top:55px;width:82px">Our clinicians bring calm, practiced hands to every visit, giving families the confidence to seek care early and often, close to home.</div>
  <div class="card" style="left:21px;top:92px;width:83px;height:16px"></div>
  <div class="abs red" style="left:27px;top:96px;font-size:7px">82%</div>
  <div class="abs red" style="left:46px;top:97px;font-size:2.4px;line-height:1.2">Happy<br>Patient</div>
  <div class="abs red" style="left:65px;top:96px;font-size:7px">70+</div>
  <div class="abs red" style="left:84px;top:97px;font-size:2.4px;line-height:1.2">Success<br>Surgery</div>
  <div class="photo blue" role="img" aria-label="Doctor giving a high five to a young boy" style="left:124px;top:22px;width:104px;height:94px;border-radius:3px 0 0 3px"></div>
</section>

<section class="slide" style="left:258px;top:664px">
  <div class="photo warm" role="img" aria-label="Diagonal strips of portraits of healthcare staff" style="left:0;top:0;width:108px;height:128px;clip-path:polygon(0 20%,30% 0,100% 100%,55% 100%,0 40%)"></div>
  <div class="photo" role="img" aria-label="Stethoscope on a desk" style="left:0;top:0;width:108px;height:128px;clip-path:polygon(32% 0,52% 0,80% 38%,70% 52%)"></div>
  <div class="logo" style="left:167px;top:10px">Larkfell</div>
  <div class="kicker" style="left:107px;top:29px;font-size:6px;font-weight:500">OUR JOURNEY</div>
  <div class="abs box white" style="left:107px;top:40px;width:10px;height:10px;border-radius:50%;font-size:4px;text-align:center;line-height:10px">01</div>
  <div class="abs" style="left:123px;top:42px;font-size:4.6px">Our Mission</div>
  <div class="t" style="left:123px;top:50px;width:95px;font-size:2.9px">Larkfell is devoted to strengthening rural care by giving providers tailored staffing that lifts capability and supports community health.</div>
  <div class="abs box white" style="left:107px;top:78px;width:10px;height:10px;border-radius:50%;font-size:4px;text-align:center;line-height:10px">02</div>
  <div class="abs" style="left:123px;top:80px;font-size:4.6px">Core Values</div>
  <div class="t" style="left:123px;top:88px;width:95px;font-size:2.9px">Integrity, teamwork and fresh thinking guide all we do. We build strong ties with clinics and drive positive change through tailored solutions.</div>
</section>

<section class="slide" style="left:498px;top:664px">
  <div class="abs" style="left:22px;top:12px;display:grid;grid-template-columns:repeat(10,19px);grid-auto-rows:13.6px;align-items:center;justify-items:center">
    <i class="glyph"></i><i class="glyph" style="border-radius:50%"></i><i class="glyph"></i><i class="glyph" style="width:3px"></i><i class="glyph" style="border-radius:50%"></i><i class="glyph"></i><i class="glyph" style="border-radius:50%"></i><i class="glyph"></i><i class="glyph" style="height:3px"></i><i class="glyph" style="border-radius:50%"></i>
    <i class="glyph"></i><i class="glyph" style="width:3px"></i><i class="glyph"></i><i class="glyph"></i><i class="glyph" style="border-radius:50%"></i><i class="glyph"></i><i class="glyph" style="height:3px"></i><i class="glyph"></i><i class="glyph" style="border-radius:50%"></i><i class="glyph" style="border-radius:50% 50% 50% 0"></i>
    <i class="glyph" style="border-radius:50%"></i><i class="glyph"></i><i class="glyph"></i><i class="glyph" style="width:3px"></i><i class="glyph" style="width:3px"></i><i class="glyph"></i><i class="glyph"></i><i class="glyph" style="border-radius:50%"></i><i class="glyph"></i><i class="glyph"></i>
    <i class="glyph"></i><i class="glyph" style="border-radius:50%"></i><i class="glyph"></i><i class="glyph" style="border-radius:50%"></i><i class="glyph" style="height:3px"></i><i class="glyph"></i><i class="glyph"></i><i class="glyph"></i><i class="glyph" style="border-radius:50%"></i><i class="glyph" style="width:3px"></i>
    <i class="glyph"></i><i class="glyph" style="width:3px"></i><i class="glyph" style="border-radius:50%"></i><i class="glyph"></i><i class="glyph"></i><i class="glyph" style="border-radius:50% 50% 0 0"></i><i class="glyph" style="border-radius:50%"></i><i class="glyph"></i><i class="glyph" style="width:3px"></i><i class="glyph"></i>
    <i class="glyph"></i><i class="glyph" style="border-radius:50%"></i><i class="glyph"></i><i class="glyph" style="border-radius:50%"></i><i class="glyph"></i><i class="glyph" style="border-radius:50%"></i><i class="glyph"></i><i class="glyph" style="width:3px"></i><i class="glyph" style="border-radius:50%"></i><i class="glyph"></i>
    <i class="glyph" style="width:3px"></i><i class="glyph" style="border-radius:50%"></i><i class="glyph"></i><i class="glyph" style="height:3px"></i><i class="glyph"></i><i class="glyph"></i><i class="glyph" style="width:3px"></i><i class="glyph" style="border-radius:50%"></i><i class="glyph" style="width:3px"></i><i class="glyph" style="border-radius:50% 50% 0 0"></i>
    <i class="glyph" style="width:3px"></i><i class="glyph" style="height:3px"></i><i class="glyph"></i><i class="glyph"></i><i class="glyph" style="border-radius:50%"></i><i class="glyph" style="border-radius:50%"></i><i class="glyph"></i><i class="glyph"></i><i class="glyph" style="border-radius:50%"></i><i class="glyph" style="border-radius:50% 50% 0 0"></i>
  </div>
</section>

<!-- Row 7 -->
<section class="slide" style="left:17px;top:794px">
  <div class="box" style="left:0;top:0;width:228px;height:128px"></div>
  <div class="photo" role="img" aria-label="Smiling doctor holding a clipboard" style="left:35px;top:20px;width:102px;height:108px;border-radius:2px 2px 0 0"></div>
  <div class="title white" style="left:120px;top:30px;font-size:9.5px">Excellence In<br>Healthcare</div>
  <div class="card" style="left:74px;top:64px;width:140px;height:53px"></div>
  <div class="abs red" style="left:82px;top:71px;font-size:6px">✎</div>
  <div class="abs" style="left:94px;top:72px;font-size:3px;line-height:1.3;font-weight:500">Medicine That<br>Touches The World</div>
  <div class="abs red" style="left:147px;top:71px;font-size:6px">⚕</div>
  <div class="abs" style="left:159px;top:72px;font-size:3px;line-height:1.3;font-weight:500">Medicine That<br>Touches The World</div>
  <div class="t" style="left:80px;top:88px;width:60px;font-size:2.7px">Skilled staff who travel to the clinics that need them, ready from the very first day.</div>
  <div class="t" style="left:145px;top:88px;width:60px;font-size:2.7px">Care plans shaped with local teams so every patient gets steady, trusted support.</div>
</section>

<section class="slide" style="left:258px;top:794px">
  <div class="logo" style="left:13px;top:16px">Larkfell</div>
  <div class="title" style="left:13px;top:42px">Meet Our<br>Doctor</div>
  <div class="t" style="left:13px;top:70px;width:60px">Devoted to your well-being, each doctor pairs real compassion with years of practice to give personal, high-quality care to every patient.</div>
  <div class="photo" role="img" aria-label="Portrait of a female doctor with glasses" style="left:76px;top:19px;width:42px;height:68px"></div>
  <div class="photo" role="img" aria-label="Portrait of a smiling female doctor" style="left:123px;top:19px;width:42px;height:68px"></div>
  <div class="photo" role="img" aria-label="Portrait of a male doctor in a face mask" style="left:170px;top:19px;width:42px;height:68px"></div>
  <div class="box" style="left:76px;top:87px;width:42px;height:18px"></div>
  <div class="box" style="left:123px;top:87px;width:42px;height:18px"></div>
  <div class="box" style="left:170px;top:87px;width:42px;height:18px"></div>
  <div class="abs white" style="left:79px;top:91px;font-size:3px;line-height:2">Dr. Owen Hale<br><span style="opacity:.8">Optometry</span></div>
  <div class="abs white" style="left:126px;top:91px;font-size:3px;line-height:2">Dr. Iris Crane<br><span style="opacity:.8">Dentist</span></div>
  <div class="abs white" style="left:173px;top:91px;font-size:3px;line-height:2">Dr. Ray Lund<br><span style="opacity:.8">Pediatrics</span></div>
</section>

<section class="slide" style="left:498px;top:794px">
  <div class="photo warm" role="img" aria-label="Group of cheerful older adults laughing with a caregiver" style="left:0;top:0;width:228px;height:128px"></div>
  <div class="abs" style="left:137px;top:21px;width:40px;height:12px;background:rgba(255,255,255,.75);border-radius:2px"></div>
  <div class="logo" style="left:140px;top:23px;font-size:5px">Larkfell</div>
  <div class="title white" style="left:0;top:52px;width:228px;text-align:center;font-size:16px;font-weight:500;text-shadow:0 1px 3px rgba(0,0,0,.35)">Thank You....</div>
</section>

<!-- Row 8 -->
<section class="slide" style="left:17px;top:924px">
  <div class="box" style="left:0;top:0;width:24px;height:128px"></div>
  <div class="abs" style="left:12px;top:20px;width:54px;height:54px;border-radius:50%;background:#fff;box-shadow:0 1px 3px rgba(0,0,0,.2)"></div>
  <div class="photo dark" role="img" aria-label="Portrait of the company CEO" style="left:15px;top:23px;width:48px;height:48px;border-radius:50%"></div>
  <div class="logo" style="left:162px;top:16px">Larkfell</div>
  <div class="abs red" style="left:77px;top:44px;font-size:5px">Mark Tallis</div>
  <div class="abs" style="left:77px;top:52px;font-size:4px">Our CEO</div>
  <div class="box" style="left:56px;top:64px;width:154px;height:49px;border-radius:2px"></div>
  <div class="abs white" style="left:70px;top:75px;width:132px;font-size:5.5px;line-height:1.75;letter-spacing:.3px">Good health is not something we can buy. However, it can be an extremely valuable savings account.</div>
</section>

<section class="slide" style="left:258px;top:924px">
  <div class="photo warm" role="img" aria-label="Young girl opening her mouth for a throat check" style="left:15px;top:19px;width:85px;height:85px;border-radius:50%"></div>
  <div class="box" style="left:80px;top:67px;width:31px;height:33px;border-radius:2px;box-shadow:0 1px 3px rgba(0,0,0,.2)"></div>
  <div class="abs" style="left:91px;top:73px;width:9px;height:4px;border:1px solid #fff;border-radius:3px;transform:rotate(-40deg)"></div>
  <div class="abs white" style="left:80px;top:84px;width:31px;text-align:center;font-size:3.2px;line-height:1.3">Better<br>Medicine</div>
  <div class="logo" style="left:168px;top:10px">Larkfell</div>
  <div class="title" style="left:124px;top:33px">Always Caring,<br>Always Here</div>
  <div class="t" style="left:124px;top:58px;width:92px">Day or night, our staff stay close so rural families can count on calm, skilled care whenever they need it.</div>
  <div class="abs red" style="left:124px;top:80px;font-size:3.6px;line-height:2.3">• Genius In Healthcare<br>• Extraordinary Care<br>• Solutions For Change</div>
</section>

<!-- Row 9 -->
<section class="slide" style="left:17px;top:1054px">
  <div class="logo" style="left:23px;top:18px">Larkfell</div>
  <div class="title" style="left:23px;top:37px">Transforming<br>Healthcare</div>
  <div class="kicker" style="left:23px;top:67px;font-size:3.8px">Genius In Healthcare</div>
  <div class="t" style="left:23px;top:75px;width:86px">Better staffing means shorter waits, steadier teams and care that patients can trust, whether the clinic sits in town or far out on a county road.</div>
  <svg class="abs" style="left:118px;top:10px" width="104" height="112" viewBox="0 0 104 112">
    <g font-size="2.6" fill="#666" font-family="Rubik,sans-serif">
      <text x="0" y="8">6.3</text><text x="0" y="28">5</text><text x="0" y="45">3.8</text><text x="0" y="62">2.5</text><text x="0" y="79">1.3</text><text x="0" y="96">0</text>
      <text x="14" y="104">Category 1</text><text x="35" y="104">Category 2</text><text x="56" y="104">Category 3</text><text x="77" y="104">Category 4</text>
    </g>
    <g stroke="#eee" stroke-width=".4"><line x1="8" y1="7" x2="102" y2="7"/><line x1="8" y1="27" x2="102" y2="27"/><line x1="8" y1="44" x2="102" y2="44"/><line x1="8" y1="61" x2="102" y2="61"/><line x1="8" y1="78" x2="102" y2="78"/><line x1="8" y1="95" x2="102" y2="95"/></g>
    <rect x="14" y="63" width="7" height="32" fill="var(--red)"/><rect x="21" y="68" width="7" height="27" fill="#dcdcdc"/>
    <rect x="35" y="68" width="7" height="27" fill="var(--red)"/><rect x="42" y="35" width="7" height="60" fill="#dcdcdc"/>
    <rect x="56" y="48" width="7" height="47" fill="var(--red)"/><rect x="63" y="74" width="7" height="21" fill="#dcdcdc"/>
    <rect x="77" y="34" width="7" height="61" fill="var(--red)"/><rect x="84" y="29" width="7" height="66" fill="#dcdcdc"/>
  </svg>
</section>

<section class="slide" style="left:258px;top:1054px">
  <div class="logo" style="left:19px;top:17px">Larkfell</div>
  <div class="title" style="left:19px;top:33px;font-size:8.5px">Chosen for Excellence</div>
  <div class="t" style="left:19px;top:46px;width:102px;font-size:2.8px">Clinics pick Larkfell for steady staff, clear plans and results they can see in their own numbers.</div>
  <svg class="abs" style="left:14px;top:62px" width="115" height="56" viewBox="0 0 115 56">
    <g font-size="2.2" fill="#777" font-family="Rubik,sans-serif">
      <text x="0" y="8">Category 4</text><text x="0" y="18">Category 3</text><text x="0" y="28">Category 2</text><text x="0" y="38">Category 1</text>
      <text x="13" y="48">0</text><text x="35" y="48">3.5</text><text x="57" y="48">7</text><text x="79" y="48">10.5</text><text x="101" y="48">14</text>
    </g>
    <rect x="14" y="5.5" width="90" height="3.5" fill="#e2e2e2"/><rect x="14" y="5.5" width="29" height="3.5" fill="var(--red)"/>
    <rect x="14" y="15.5" width="56" height="3.5" fill="#e2e2e2"/><rect x="14" y="15.5" width="22" height="3.5" fill="var(--red)"/>
    <rect x="14" y="25.5" width="98" height="3.5" fill="#e2e2e2"/><rect x="14" y="25.5" width="16" height="3.5" fill="var(--red)"/>
    <rect x="14" y="35.5" width="70" height="3.5" fill="#e2e2e2"/><rect x="14" y="35.5" width="28" height="3.5" fill="var(--red)"/>
  </svg>
  <div class="box" style="left:141px;top:15px;width:65px;height:26px;border-radius:2px"></div>
  <div class="box" style="left:141px;top:50px;width:65px;height:26px;border-radius:2px"></div>
  <div class="box" style="left:141px;top:86px;width:65px;height:26px;border-radius:2px"></div>
  <div class="abs white" style="left:147px;top:20px;font-size:7.5px">81%</div>
  <div class="abs white" style="left:147px;top:55px;font-size:7.5px">63%</div>
  <div class="abs white" style="left:147px;top:91px;font-size:7.5px">76%</div>
  <div class="abs white" style="left:147px;top:31px;font-size:3px;opacity:.85">per-year</div>
  <div class="abs white" style="left:147px;top:66px;font-size:3px;opacity:.85">per-year</div>
  <div class="abs white" style="left:147px;top:102px;font-size:3px;opacity:.85">per-year</div>
  <div class="t w" style="left:170px;top:20px;width:32px;font-size:2.2px">Clinics that renewed their plan this year.</div>
  <div class="t w" style="left:170px;top:55px;width:32px;font-size:2.2px">Shifts filled within one week of request.</div>
  <div class="t w" style="left:170px;top:91px;width:32px;font-size:2.2px">Staff who stay on past their first year.</div>
</section>

</body>
</html>
```